Dean wants a Kick arse Business card

Launching my new company Harrow Real Estate 1st July, and will be mailing out to past clients, need a kick arse business card design pronto to get printing done in time for mail out
I'm after a two sided card - one side for all contact details (see below) the other side for impact (kick arsery!)
Logo and my photo attached, details to go onto card are as follows
Dean Harrow - Principal
M: 0412 905 364
E: dean@harrowre.com.au
Dean Harrow Real Estate Pty Ltd trading as Harrow Real Estate
Licensed Real Estate & Business Agents
ABN 42 803 517 296 Triennial Cert No. RA31472
14 Marbrook Avenue, Kelmscott WA 6111
Tel: 08 9371 6048 Fax: 08 6209 4812

```html
<!DOCTYPE html>
<html lang="en">
<head>
<meta charset="utf-8">
<title>Harrow Real Estate – Business Card</title>
<link href="https://fonts.googleapis.com/css2?family=Open+Sans:wght@300;400;700&display=swap" rel="stylesheet">
<style>
  :root {
    --canvas: #ebecec;
    --card: #ffffff;
    --navy: #0d4a78;
    --ink: #2b2b2b;
    --ink-soft: #3a3a3a;
    --band-top: #0a4a77;
    --band-bottom: #1d9fdc;
    --rule: #0d5a8c;
    --brand: #136fae;
    --photo-top: #d9dadc;
    --photo-bottom: #2a2c30;
  }
  * { box-sizing: border-box; margin: 0; padding: 0; }
  html, body { width: 1049px; height: 1200px; overflow: hidden; }
  body {
    background: var(--canvas);
    font-family: "Open Sans", Arial, sans-serif;
    position: relative;
  }
  .card {
    position: absolute;
    left: 132px;
    width: 772px;
    height: 457px;
    background: var(--card);
    border-radius: 22px;
    overflow: hidden;
    box-shadow: 0 4px 10px rgba(0,0,0,0.18);
  }
  .card--front { top: 72px; }
  .card--back { top: 625px; }

  .rule {
    position: absolute; left: 0; right: 0;
    top: 350px; height: 4px;
    background: var(--rule);
  }
  .band {
    position: absolute; left: 0; right: 0;
    top: 363px; bottom: 0;
    background: linear-gradient(to bottom, var(--band-top), var(--band-bottom));
    display: flex; align-items: center; justify-content: center;
    color: #fff; font-weight: 700;
  }

  .portrait {
    position: absolute; left: 34px; top: 31px;
    width: 235px; height: 332px;
    background: linear-gradient(to bottom, var(--photo-top) 0%, #b9a89a 35%, var(--photo-bottom) 60%);
  }

  .brand {
    display: flex; align-items: center; gap: 12px;
    color: var(--navy);
    font-weight: 700;
  }
  .brand__dot {
    width: 44px; height: 44px; border-radius: 50%;
    background: var(--brand); flex: none;
  }
  .brand__name { font-size: 26px; line-height: 1.1; }
  .card--front .brand { position: absolute; left: 470px; top: 70px; }
  .card--back .brand { position: absolute; left: 0; right: 0; top: 70px; justify-content: center; }

  .agent { position: absolute; left: 312px; top: 208px; color: var(--ink); }
  .agent__name { font-size: 25px; font-weight: 700; line-height: 32px; }
  .agent__role { font-size: 25px; font-weight: 300; line-height: 32px; }
  .agent__mobile {
    margin-top: 26px;
    display: flex; align-items: center; gap: 14px;
    font-size: 26px; font-weight: 700;
  }

  .email { font-size: 26px; gap: 14px; top: 363px; }

  .entity {
    position: absolute; left: 0; right: 0; top: 173px;
    text-align: center; color: var(--navy);
    font-size: 22px; font-weight: 700; line-height: 30px;
  }
  .contacts {
    position: absolute; left: 118px; top: 250px;
    list-style: none; color: var(--ink-soft);
    font-size: 20px; font-weight: 400;
  }
  .contacts li {
    display: flex; align-items: center; height: 30px; gap: 10px;
  }
  .contacts svg { width: 26px; height: 24px; flex: none; }

  .legal { font-size: 22px; }
</style>
</head>
<body>

<section class="card card--front">
  <div class="portrait" role="img" aria-label="Portrait photo of Dean Harrow"></div>

  <div class="brand">
    <span class="brand__dot"></span>
    <span class="brand__name">Harrow Real Estate</span>
  </div>

  <div class="agent">
    <p class="agent__name">Dean Harrow</p>
    <p class="agent__role">Principal</p>
    <p class="agent__mobile">
      <svg width="18" height="26" viewBox="0 0 18 26" aria-hidden="true">
        <rect x="1.5" y="1.5" width="15" height="23" rx="2.5" fill="none" stroke="#2b2b2b" stroke-width="2.2"/>
        <line x1="1.5" y1="19" x2="16.5" y2="19" stroke="#2b2b2b" stroke-width="2"/>
        <circle cx="9" cy="21.8" r="1.2" fill="#2b2b2b"/>
      </svg>
      0412 905 364
    </p>
  </div>

  <div class="rule"></div>
  <div class="band email">
    <svg width="32" height="22" viewBox="0 0 32 22" aria-hidden="true">
      <rect x="1.5" y="1.5" width="29" height="19" fill="none" stroke="#fff" stroke-width="2.2"/>
      <polyline points="1.5,1.5 16,13 30.5,1.5" fill="none" stroke="#fff" stroke-width="2.2"/>
      <polyline points="1.5,20.5 12,10.5 M20,10.5 30.5,20.5" fill="none" stroke="#fff" stroke-width="2"/>
    </svg>
    dean@harrowre.com.au
  </div>
</section>

<section class="card card--back">
  <div class="brand">
    <span class="brand__dot"></span>
    <span class="brand__name">Harrow Real Estate</span>
  </div>

  <div class="entity">
    <p>Dean Harrow Real Estate Pty Ltd trading as Harrow Real Estate</p>
    <p>Licensed Real Estate &amp; Business Agents</p>
  </div>

  <ul class="contacts">
    <li>
      <svg viewBox="0 0 26 24" aria-hidden="true">
        <polygon points="13,2 25,9 1,9" fill="#333"/>
        <rect x="3" y="9" width="20" height="13" fill="#333"/>
        <rect x="10" y="13" width="6" height="9" fill="#fff"/>
      </svg>
      14 Marbrook Avenue, Kelmscott WA 6111
    </li>
    <li>
      <svg viewBox="0 0 26 24" aria-hidden="true">
        <path d="M7 2 L10 2 L11 8 L8.5 9.5 C10 13.5 12 16 15.5 17.5 L17 15 L23 16 L23 20 C23 21 22 22 21 22 C11 21 5 14 5 4 C5 3 6 2 7 2 Z" fill="#333"/>
      </svg>
      08 9371 6048
    </li>
    <li>
      <svg viewBox="0 0 26 24" aria-hidden="true">
        <rect x="7" y="1" width="12" height="8" fill="none" stroke="#333" stroke-width="1.6"/>
        <rect x="2" y="9" width="22" height="13" rx="2" fill="#333"/>
        <rect x="6" y="13" width="14" height="3" fill="#fff"/>
      </svg>
      08 6209 4812
    </li>
  </ul>

  <div class="rule"></div>
  <div class="band legal">ABN 42 803 517 296 Triennial Cert No. RA31472</div>
</section>

</body>
</html>
```